Stonebay Towing Business Card

Towing
Accident towing
Mechanical breakdown
Insurance, salvage and recovery
4wd off road towing
Light & Heavy towing
8347 2516
24 hour business 7 days

Logo can be whole size on front

Industry/Entity Type

Towing/ transport

Contact Information for Business Card

The above

```html
<!DOCTYPE html>
<html lang="en">
<head>
<meta charset="utf-8">
<title>Stonebay Towing Business Card</title>
<link rel="stylesheet" href="https://fonts.googleapis.com/css2?family=Montserrat:wght@700;800&family=Roboto+Condensed:wght@500;700&display=swap">
<style>
  :root {
    --brand-red: #b71c24;
    --brand-red-dark: #a3161d;
    --ink: #1a1a1a;
    --card-white: #f1f1f1;
    --backdrop: #d6d6d4;
    --on-red: #ffffff;
  }
  * { box-sizing: border-box; margin: 0; padding: 0; }
  html, body { width: 1200px; height: 765px; overflow: hidden; }
  body {
    background: var(--backdrop);
    position: relative;
    font-family: "Roboto Condensed", Arial, sans-serif;
  }
  .card {
    position: absolute;
    width: 560px;
    height: 320px;
    overflow: hidden;
  }
  .card-front {
    left: 60px; top: 60px;
    background: linear-gradient(135deg, var(--brand-red-dark), var(--brand-red));
    display: flex; align-items: center; justify-content: center;
  }
  .front-name {
    color: var(--on-red);
    font-family: "Roboto Condensed", Arial, sans-serif;
    font-weight: 700;
    font-size: 58px;
    letter-spacing: 0.5px;
  }
  .card-back {
    left: 580px; top: 385px;
    background: var(--card-white);
  }
  .back-graphics { position: absolute; inset: 0; }
  .badge-number {
    position: absolute; left: 50px; top: 54px;
    font-family: "Montserrat", Arial, sans-serif; font-weight: 800;
    font-size: 38px; color: var(--brand-red); letter-spacing: -2px;
  }
  .badge-hours {
    position: absolute; left: 89px; top: 103px;
    font-family: "Montserrat", Arial, sans-serif; font-weight: 700;
    font-size: 7.5px; color: var(--on-red);
  }
  .badge-service {
    position: absolute; left: 115px; top: 67px;
    font-family: "Montserrat", Arial, sans-serif; font-weight: 800;
    font-size: 21px; color: var(--ink);
  }
  .badge-everyday {
    position: absolute; left: 164px; top: 94px;
    font-family: "Montserrat", Arial, sans-serif; font-weight: 800;
    font-size: 9px; color: var(--ink);
  }
  .phone-number {
    position: absolute; left: 312px; top: 97px;
    font-family: "Roboto Condensed", Arial, sans-serif; font-weight: 700;
    font-size: 26px; letter-spacing: 3px; color: var(--on-red);
  }
  .service-list {
    position: absolute; left: 38px; top: 146px;
    list-style: none;
  }
  .service-list li {
    display: flex; align-items: center;
    height: 29.6px;
    font-weight: 500; font-size: 16.5px; color: var(--ink);
  }
  .service-list svg { width: 14px; height: 12px; margin-right: 12px; }
  .back-name {
    position: absolute; right: 30px; top: 228px;
    color: var(--brand-red);
    font-family: "Roboto Condensed", Arial, sans-serif;
    font-weight: 700; font-size: 26px;
  }
</style>
</head>
<body>

<section class="card card-front">
  <p class="front-name">Stonebay Towing</p>
</section>

<section class="card card-back">
  <svg class="back-graphics" viewBox="0 0 560 320" aria-hidden="true">
    <path d="M112 127 A50 50 0 1 1 104 37" fill="none" stroke="var(--brand-red)" stroke-width="3.5"/>
    <polygon points="102,28 118,38 102,45" fill="var(--brand-red)"/>
    <polygon points="86,101 132,101 140,113 86,113" fill="var(--brand-red)"/>
    <line x1="142" y1="114" x2="300" y2="114" stroke="var(--brand-red)" stroke-width="2"/>
    <rect x="298" y="96" width="210" height="36" rx="18" fill="var(--brand-red)"/>
    <circle cx="505" cy="114" r="27" fill="var(--brand-red)"/>
    <circle cx="505" cy="114" r="19" fill="none" stroke="var(--on-red)" stroke-width="3"/>
    <path d="M498 104 l4 -1 l3 6 l-3 2 q2 5 6 7 l2 -3 l6 3 l-1 4 q-2 3 -6 2 q-11 -4 -14 -15 q0 -4 3 -5z" fill="var(--on-red)"/>
  </svg>

  <span class="badge-number">24</span>
  <span class="badge-hours">HOURS</span>
  <span class="badge-service">SERVICE</span>
  <span class="badge-everyday">EVERYDAY</span>
  <span class="phone-number">8347 2516</span>

  <ul class="service-list">
    <li><svg viewBox="0 0 14 12"><path d="M1 1l5 5-5 5M7 1l5 5-5 5" fill="none" stroke="var(--brand-red)" stroke-width="2.4"/></svg>Towing | Accident towing</li>
    <li><svg viewBox="0 0 14 12"><path d="M1 1l5 5-5 5M7 1l5 5-5 5" fill="none" stroke="var(--brand-red)" stroke-width="2.4"/></svg>Mechanical breakdown</li>
    <li><svg viewBox="0 0 14 12"><path d="M1 1l5 5-5 5M7 1l5 5-5 5" fill="none" stroke="var(--brand-red)" stroke-width="2.4"/></svg>Insurance, salvage and recovery</li>
    <li><svg viewBox="0 0 14 12"><path d="M1 1l5 5-5 5M7 1l5 5-5 5" fill="none" stroke="var(--brand-red)" stroke-width="2.4"/></svg>4wd off road towing</li>
    <li><svg viewBox="0 0 14 12"><path d="M1 1l5 5-5 5M7 1l5 5-5 5" fill="none" stroke="var(--brand-red)" stroke-width="2.4"/></svg>Light &amp; Heavy towing</li>
  </ul>

  <p class="back-name">Stonebay Towing</p>
</section>

</body>
</html>
```